TBrenwick Business Cards & Letterhead

I have a logo but need a design for some new business cards. We are a Design-Build Firm that specializes in the design and construction of commercial projects.
the cards need to be professional. no cartoon stuff.
i would like to have the cards in AI format so I can update the card as needed. Logo is provided.
Our Address is: 4718 Fenmoor Ct. Elmhaven, North Carolina 27599

```html
<!DOCTYPE html>
<html lang="en">
<head>
<meta charset="UTF-8">
<title>TBrenwick Business Card</title>
<link rel="stylesheet" href="https://fonts.googleapis.com/css2?family=Open+Sans:wght@400;600;700;800&display=swap">
<style>
  :root {
    --backdrop: #333333;
    --card-dark: #212126;
    --blue-deep: #0a3a62;
    --blue-mid: #0d4f86;
    --blue-bright: #137cc0;
    --logo-grey: #5b5c61;
    --white: #ffffff;
    --icon-blue: #2c76b8;
  }
  * { margin: 0; padding: 0; box-sizing: border-box; }
  html, body {
    width: 1200px; height: 780px; overflow: hidden;
    background: var(--backdrop);
    font-family: "Open Sans", Arial, sans-serif;
  }
  .canvas {
    width: 1200px; height: 780px;
    display: flex; align-items: center; justify-content: center; gap: 40px;
  }
  .card {
    position: relative;
    width: 560px; height: 320px;
    border-radius: 22px;
    overflow: hidden;
  }

  /* Back side */
  .card-back {
    background: radial-gradient(ellipse at 50% 50%, var(--blue-bright) 0%, var(--blue-mid) 45%, var(--blue-deep) 100%);
    display: flex; align-items: center; justify-content: center; gap: 14px;
  }
  .back-mark {
    width: 30px; height: 30px;
    background: var(--blue-deep);
  }
  .back-name {
    font-weight: 800; font-size: 50px; letter-spacing: 2px;
    color: var(--blue-deep);
  }

  /* Front side */
  .card-front { background: var(--card-dark); }
  .brand-panel {
    position: absolute; left: 0; top: 36px;
    width: 232px; height: 248px;
    border-radius: 0 30px 0 30px;
    background: linear-gradient(160deg, var(--blue-bright) 0%, var(--blue-mid) 55%, var(--blue-deep) 100%);
  }
  .front-logo {
    position: absolute; right: 40px; top: 40px;
    display: flex; align-items: center; gap: 10px;
  }
  .front-logo-mark { width: 18px; height: 18px; background: var(--blue-mid); }
  .front-logo-name {
    font-weight: 800; font-size: 34px; letter-spacing: 1px;
    color: var(--logo-grey);
  }
  .name-band {
    position: absolute; left: 250px; right: 0; top: 104px; height: 56px;
    background: linear-gradient(90deg, rgba(13,79,134,0) 0%, var(--blue-mid) 40%, var(--blue-mid) 100%);
    text-align: right; padding: 6px 26px 0 0;
    color: var(--white);
  }
  .person-name { font-weight: 800; font-size: 24px; letter-spacing: 1px; line-height: 1.1; }
  .person-title { font-weight: 600; font-size: 14px; line-height: 1.3; }
  .address {
    position: absolute; right: 26px; top: 172px;
    text-align: right; color: var(--white);
    font-size: 14px; line-height: 1.35; font-weight: 600;
  }
  .contact-list {
    position: absolute; right: 20px; top: 222px;
    list-style: none; color: var(--white);
    font-size: 14px; font-weight: 600; line-height: 1.4;
  }
  .contact-list li { display: flex; justify-content: flex-end; align-items: center; gap: 8px; }
  .contact-icon { width: 13px; height: 13px; }
</style>
</head>
<body>
<main class="canvas">
  <section class="card card-back" aria-label="Card back">
    <span class="back-mark"></span>
    <span class="back-name">TBRENWICK</span>
  </section>

  <section class="card card-front" aria-label="Card front">
    <div class="brand-panel" role="img" aria-label="Large brand symbol area in blue gradient"></div>

    <div class="front-logo">
      <span class="front-logo-mark"></span>
      <span class="front-logo-name">TBRENWICK</span>
    </div>

    <div class="name-band">
      <p class="person-name">DARREN BRENWICK</p>
      <p class="person-title">Founder/President</p>
    </div>

    <p class="address">4718 Fenmoor Ct. Elmhaven,<br>North Carolina 27599</p>

    <ul class="contact-list">
      <li>(919) 555-0148
        <svg class="contact-icon" viewBox="0 0 16 16" aria-hidden="true"><path fill="var(--icon-blue)" d="M3.5 1.5l2.5 0 1 3.5-1.6 1.1a8 8 0 0 0 4.5 4.5L11 9l3.5 1v2.5a2 2 0 0 1-2 2A11 11 0 0 1 1.5 3.5a2 2 0 0 1 2-2z"/></svg>
      </li>
      <li>www.tbrenwick.com
        <svg class="contact-icon" viewBox="0 0 16 16" aria-hidden="true"><g fill="none" stroke="var(--icon-blue)" stroke-width="1.5"><circle cx="8" cy="8" r="6.5"/><ellipse cx="8" cy="8" rx="2.8" ry="6.5"/><line x1="1.5" y1="8" x2="14.5" y2="8"/></g></svg>
      </li>
      <li>DSB@TBrenwick.com
        <svg class="contact-icon" viewBox="0 0 16 16" aria-hidden="true"><g fill="none" stroke="var(--icon-blue)" stroke-width="1.5"><rect x="1.5" y="3.5" width="13" height="9" rx="1"/><polyline points="1.5,4 8,9 14.5,4"/></g></svg>
      </li>
    </ul>
  </section>
</main>
</body>
</html>
```